Bref créative
PinTroller.net Web Template
Web Template
Advertising
"We put advertising on the bottom of the receipts for restaurants and
bars."
Like main navigation at the top. Like things kept clean and simple.
Clean/Simple
match color scheme of logo
above header
www.dorvelautospa.example
1) Need a place for users to login or sign up if they aren't members.
2) Navigation should be: Home, Advertise, Register, Partners, About Us
3) Content on the page should be in two columns.
4) Footer should have a link called "Contact Us"
5) Deign of template should tie in with our logo.
logo file
JPEG of the Logo
Here is the best header image so far. I'd like the header image to look like this if possible. I like the water mark on the right and the "Get Started" Button. I would like the add on the receipt to be for a car wash called Dorvel Auto Spa. www.dorvelautospa.example
Here is the artwork for the car wash logo that should be on the ad
Here is a screenshot of the best layout. I'd like to have something similar to this layout with the header image I've uploaded. Please don't copy exactly, but this gives a good idea of what I'm looking for.
Here is an example of the ad for the car wash that goes on receipts. This one is in color and the ad on the receipt should be BLACK and WHITE only. Feel free to remove whatever so you can make this smaller and fit into the image. This is just an example.

```html
<!DOCTYPE html>
<html lang="en">
<head>
<meta charset="utf-8">
<title>PinTroller</title>
<link href="https://fonts.googleapis.com/css2?family=Open+Sans:wght@400;600;700&display=swap" rel="stylesheet">
<style>
:root{
  --orange:#f29a1f;
  --yellow:#fbc02d;
  --red:#c8202f;
  --grey-box:#a9a9a9;
  --dark:#3a3a3a;
  --text:#8a8a8a;
  --brown:#8a5a3a;
  --line:#e2e2e2;
  --link:#d2202f;
}
*{box-sizing:border-box;margin:0;padding:0}
html,body{width:1200px;height:896px;overflow:hidden;background:#fff}
body{position:relative;font-family:"Open Sans",Arial,sans-serif;color:var(--text)}
.page-glow{position:absolute;left:100px;top:0;width:1000px;height:896px;background:linear-gradient(#fff,#f7f7f7 60%,#fff)}
.site-name{position:absolute;left:156px;top:104px;font-weight:600;font-size:22px;line-height:30px;color:#444}
.main-nav{position:absolute;top:113px;left:320px;display:flex}
.nav-item{width:150px;height:48px;padding:6px 16px;border-left:1px solid var(--line)}
.nav-item:first-child{border-left:none}
.nav-title{display:block;font-size:15px;color:var(--orange);line-height:18px}
.nav-sub{display:block;font-size:11px;color:#888;line-height:16px}
.nav-item.active{background:#d9d9d9;border-radius:8px 8px 0 0}
.nav-item.active .nav-title{color:var(--red);font-weight:600}
.dropdown{position:absolute;left:758px;top:163px;width:135px;height:96px;background:var(--dark);border-radius:0 0 8px 8px;padding:8px 12px;z-index:2}
.dropdown a{display:block;color:#fff;font-size:11px;font-weight:600;line-height:17px;text-decoration:none}
.hero{position:absolute;left:144px;top:168px;width:900px;height:312px;border-radius:18px;overflow:hidden;
  background:radial-gradient(ellipse at 62% 70%,#3c3c3c 0,#8d8d8d 18%,#d8d8d8 38%,#a2a2a2 55%,#e6e6e6 75%,#bcbcbc 100%)}
.hero-tag{position:absolute;left:149px;top:211px;height:40px;width:278px;background:var(--yellow);border-radius:6px 6px 0 0;color:#fff;font-size:25px;font-weight:600;padding-left:14px;line-height:40px}
.hero-follow{position:absolute;left:149px;top:252px;width:103px;height:36px;background:#fff;border-radius:0 0 6px 6px;color:#222;font-size:18px;font-weight:700;line-height:36px;text-align:center}
.arrow{position:absolute;top:296px}
.arrow-left{left:100px}.arrow-right{left:1056px}
.feature{position:absolute;top:492px;width:295px;height:137px;padding:14px 22px;color:#fff}
.feature h2{font-size:21px;font-weight:700;line-height:28px;color:#444}
.feature p{font-size:13px;line-height:18px;width:190px;margin-top:6px}
.feature-member{left:144px;background:var(--yellow)}
.feature-member p{color:#7a5a10}
.feature-services{left:451px;background:var(--grey-box)}
.feature-services p{color:#eee}
.feature-where{left:754px;background:var(--red)}
.feature-where h2{color:#f3a0a0}
.feature-where p{color:#f7d0d0}
.plus{position:absolute;right:24px;bottom:-20px;width:62px;height:62px;border-radius:50%;border:6px solid #fff;display:flex;align-items:center;justify-content:center;color:#111;font-size:32px;font-weight:400}
.feature-member .plus{background:var(--yellow)}
.feature-services .plus{background:var(--grey-box)}
.feature-where .plus{background:var(--red)}
.login{position:absolute;left:144px;top:662px;width:288px;height:240px;border:1px solid var(--line);background:#fff}
.login-head{height:62px;border-bottom:1px solid var(--line);display:flex;align-items:center;padding-left:60px;gap:20px;font-size:17px;color:#444;background:linear-gradient(#fff,#f2f2f2)}
.login-icon{width:26px;height:26px;border-radius:50%;border:1px solid #ccc;background:#f4f4f4;font-size:11px;text-align:center;line-height:24px;color:#777}
.login label{display:block;margin:18px 0 0 26px;font-size:14px;color:#222}
.login input{display:block;margin:6px 0 0 26px;width:238px;height:34px;border:1px solid #bbb;border-radius:10px}
.divider{position:absolute;top:660px;width:1px;height:240px;background:var(--line)}
.welcome{position:absolute;left:461px;top:672px;width:262px}
.welcome h1{font-size:34px;font-weight:400;color:var(--yellow);line-height:48px}
.welcome p{font-size:13px;line-height:19px;margin-top:14px;color:#8a8a8a}
.link-list{position:absolute;left:766px;top:730px;list-style:none}
.link-list li{height:38.5px}
.link-list a{font-size:13px;color:var(--link);text-decoration:underline}
</style>
</head>
<body>
<div class="page-glow"></div>

<div class="site-name">PinTroller</div>

<nav class="main-nav">
  <div class="nav-item"><span class="nav-title">Home</span><span class="nav-sub">Welcome</span></div>
  <div class="nav-item"><span class="nav-title">Advertising</span><span class="nav-sub">How to ...</span></div>
  <div class="nav-item"><span class="nav-title">Partners</span><span class="nav-sub">Our Partners</span></div>
  <div class="nav-item active"><span class="nav-title">About Us</span><span class="nav-sub">Our Company</span></div>
  <div class="nav-item"><span class="nav-title">Contact Us</span><span class="nav-sub">Get in touch</span></div>
</nav>
<div class="dropdown"><a href="#">&gt; What we do</a><a href="#">&gt; Who we are</a></div>

<div class="hero" role="img" aria-label="Close-up photo of a rolled paper receipt"></div>
<div class="hero-tag">See how we work</div>
<div class="hero-follow">Follow us</div>

<svg class="arrow arrow-left" width="24" height="50" viewBox="0 0 24 50"><polyline points="20,4 5,25 20,46" fill="none" stroke="var(--brown)" stroke-width="3"/></svg>
<svg class="arrow arrow-right" width="24" height="50" viewBox="0 0 24 50"><polyline points="4,4 19,25 4,46" fill="none" stroke="var(--brown)" stroke-width="3"/></svg>

<section class="feature feature-member">
  <h2>Become a member</h2>
  <p>Find more about services offered to members and how to join...</p>
  <span class="plus">+</span>
</section>
<section class="feature feature-services">
  <h2>Our Services</h2>
  <p>Find more about what we doand what we are...</p>
  <span class="plus">+</span>
</section>
<section class="feature feature-where">
  <h2>Where we are</h2>
  <p>Find more about what we doand what we are...</p>
  <span class="plus">+</span>
</section>

<form class="login">
  <div class="login-head"><span class="login-icon">&raquo;</span>User Login</div>
  <label>E-mail</label><input type="text">
  <label>Password</label><input type="password">
</form>

<div class="divider" style="left:446px"></div>
<div class="divider" style="left:748px"></div>

<section class="welcome">
  <h1>Welcome To Us</h1>
  <p>Text TextText TextText TextText TextText TextText TextText Text TextText TextText TextText Text TextText TextText Text TextText TextText TextText TextText TextText TextText TextText TextText TextText TextText TextText TextText</p>
</section>

<ul class="link-list">
  <li><a href="#">&gt; Link Link Link Link Link Link Link Link</a></li>
  <li><a href="#">&gt; Link Link Link Link Link Link Link Link</a></li>
  <li><a href="#">&gt; Link Link Link Link Link Link Link Link</a></li>
  <li><a href="#">&gt; Link Link Link Link Link Link Link Link</a></li>
</ul>
</body>
</html>
```